Unique business card design

Boutique coastal hotel suites - in need of clever stand out business card I have uploaded the logo that I had created through brand loft I want something that is clever and stands out from everyone else - 418 Marrowind Lane seldovia Alaska 99528 phone or text 907 -561-8204 www.tidewrenlodgeinn.com

Target Market(s)

Men and woman

Industry/Entity Type

Boutique coastal hotel

Contact Information for Business Card

Tidewren Lodge Kelpwater Alaska tidewren_lodge@kelpmail.com

Requirements
Must have
• Classy - clever -bold 907-561-8204 call or text

```html
<!DOCTYPE html>
<html lang="en">
<head>
<meta charset="utf-8">
<title>Tidewren Lodge – Business Card</title>
<link rel="stylesheet" href="https://fonts.googleapis.com/css2?family=Montserrat:wght@700&family=Questrial&display=swap">
<style>
  :root {
    --backdrop: #2a2a2a;
    --paper: #f1eee7;
    --navy: #2b4e6e;
    --red: #d1232a;
    --ink-grey: #606062;
    --rule: #5a7389;
  }
  * { margin: 0; padding: 0; box-sizing: border-box; }
  html, body {
    width: 1200px; height: 527px; overflow: hidden;
    background: var(--backdrop);
    font-family: "Questrial", sans-serif;
  }
  .canvas { position: relative; width: 1200px; height: 527px; }
  .card {
    position: absolute; top: 125px;
    width: 461px; height: 277px;
    background: var(--paper);
    box-shadow: 0 3px 8px rgba(0,0,0,.45);
  }
  .card--front { left: 106px; }
  .card--back { left: 634px; }

  .brand-name {
    position: absolute; left: 0; right: 0;
    text-align: center;
    color: var(--navy);
    font-family: "Questrial", sans-serif;
    font-weight: 400;
    letter-spacing: 2px;
    white-space: nowrap;
  }
  .card--front .brand-name { top: 120px; font-size: 26px; }
  .card--back .brand-name { top: 70px; font-size: 24px; }

  .rule { position: absolute; background: var(--rule); }
  .rule--top { left: 61px; top: 129px; width: 338px; height: 1px; }
  .rule--bottom { left: 61px; top: 206px; width: 338px; height: 1px; }
  .rule--divider { left: 182px; top: 137px; width: 1px; height: 56px; }

  .holder { position: absolute; right: 287px; top: 148px; text-align: right; }
  .holder__name {
    font-family: "Montserrat", sans-serif; font-weight: 700;
    font-size: 21px; color: var(--navy); line-height: 1; letter-spacing: -.4px;
  }
  .holder__title { font-size: 13px; color: var(--ink-grey); margin-top: 3px; }

  .contact-list { position: absolute; left: 192px; top: 139px; list-style: none; }
  .contact-list li {
    display: flex; align-items: center; gap: 5px;
    height: 17px; font-size: 13px; color: var(--ink-grey);
  }
  .icon { width: 11px; height: 11px; flex: none; }

  .address {
    position: absolute; left: 0; right: 0; top: 213px;
    display: flex; justify-content: center; align-items: center; gap: 7px;
    font-size: 16px; color: var(--ink-grey); white-space: nowrap;
  }
  .address .icon { width: 13px; height: 13px; }
</style>
</head>
<body>
<div class="canvas">

  <section class="card card--front">
    <div class="brand-name">TIDEWREN LODGE</div>
  </section>

  <section class="card card--back">
    <div class="brand-name">TIDEWREN LODGE</div>

    <div class="rule rule--top"></div>

    <div class="holder">
      <div class="holder__name">JOHN DOE</div>
      <div class="holder__title">Mangaer</div>
    </div>

    <div class="rule rule--divider"></div>

    <ul class="contact-list">
      <li>
        <svg class="icon" viewBox="0 0 12 12" aria-hidden="true"><circle cx="6" cy="6" r="6" fill="#d1232a"/><path d="M4 3.2l1 1.3-.6.7c.4.9 1.1 1.6 2 2l.7-.6 1.3 1-.7 1.1C5.7 8.6 3.4 6.3 3.3 4z" fill="#fff"/></svg>
        <span>907 -561-8204</span>
      </li>
      <li>
        <svg class="icon" viewBox="0 0 12 12" aria-hidden="true"><circle cx="6" cy="6" r="6" fill="#d1232a"/><rect x="3" y="4" width="6" height="4.2" fill="#fff"/><path d="M3 4l3 2.3L9 4" fill="none" stroke="#d1232a" stroke-width=".7"/></svg>
        <span>907 -561-8204</span>
      </li>
      <li>
        <svg class="icon" viewBox="0 0 12 12" aria-hidden="true"><circle cx="6" cy="6" r="6" fill="#d1232a"/><g fill="none" stroke="#fff" stroke-width=".7"><circle cx="6" cy="6" r="3.4"/><ellipse cx="6" cy="6" rx="1.5" ry="3.4"/><path d="M2.6 6h6.8M3.1 4.3h5.8M3.1 7.7h5.8"/></g></svg>
        <span>www.tidewrenlodgeinn.com</span>
      </li>
    </ul>

    <div class="rule rule--bottom"></div>

    <div class="address">
      <svg class="icon" viewBox="0 0 12 12" aria-hidden="true"><circle cx="6" cy="6" r="6" fill="#d1232a"/><path d="M6 2.8L2.9 5.6h.9v3h1.6V6.9h1.2v1.7h1.6v-3h.9z" fill="#fff"/></svg>
      <span>418 Marrowind Lane kelpwater Alaska 99528</span>
    </div>
  </section>

</div>
</body>
</html>
```